I need some Graphic Design for high end Japanese Restaurant Menu

Our client is a high end Japanese restaurant and wants to do a menu for food and another smaller menu for drinks. We want to have some designs for the food and some designs for the drinks to show our client. You can use sample stock pictures just for illustration first.

Attached are some samples of fine dining menu which you can modify from and improve on :

http://www.tobaremizuho.com.sg/en/

```html
<!DOCTYPE html>
<html lang="en">
<head>
<meta charset="utf-8">
<title>Tsukiha Dining – Menu Cover</title>
<link rel="stylesheet" href="https://fonts.googleapis.com/css2?family=Arimo:wght@400;700&family=Tinos:wght@700&display=swap">
<style>
  :root {
    --backdrop: #e6e6e6;
    --paper: #f7f6f3;
    --paper-edge: #ecebe7;
    --ink: #0d0d0d;
    --white: #ffffff;
    --petal: #f2a7c3;
    --photo-warm: #8a5a3c;
    --photo-cool: #6d7a72;
    --photo-dark: #3b3a38;
  }
  * { box-sizing: border-box; margin: 0; padding: 0; }
  html, body { width: 1200px; height: 983px; overflow: hidden; }
  body { background: var(--backdrop); position: relative; font-family: "Arimo", Arial, sans-serif; }

  .panel {
    position: absolute; top: 127px; width: 409px; height: 721px;
    background: radial-gradient(circle at 40% 30%, var(--paper), var(--paper-edge));
    overflow: hidden;
  }
  .panel--back { left: 193px; }
  .panel--front { left: 607px; }

  .petals {
    position: absolute; width: 130px; height: 90px;
    background: radial-gradient(ellipse at center, rgba(242,167,195,0.5), rgba(242,167,195,0) 70%);
  }
  .panel--back .petals { left: 0; top: 0; }
  .panel--front .petals { right: 0; top: 0; }

  .brand {
    position: absolute; top: 150px; left: 0; width: 100%; height: 90px;
    display: flex; justify-content: center; align-items: center; gap: 10px;
  }
  .brand__mark { width: 64px; height: 64px; background: var(--ink); flex: none; }
  .brand__name {
    font-family: "Arimo", Arial, sans-serif; font-weight: 700; font-size: 26px;
    line-height: 1.0; color: var(--ink); letter-spacing: 1px; padding-top: 14px;
  }

  .panel__base { position: absolute; left: 0; top: 480px; width: 100%; height: 241px; background: var(--ink); }

  .feature { position: absolute; width: 112px; }
  .feature__photo { height: 75px; }
  .feature__label {
    height: 15px; background: var(--white); color: var(--ink);
    font-size: 8px; font-weight: 700; text-transform: uppercase;
    text-align: center; line-height: 15px;
  }
  .feature--special { left: 19px; top: 434px; }
  .feature--special .feature__photo { background: linear-gradient(135deg, var(--photo-warm), var(--photo-dark)); }
  .feature--lunch { left: 148px; top: 421px; }
  .feature--lunch .feature__photo { background: linear-gradient(135deg, var(--photo-cool), var(--photo-warm)); }
  .feature--dinner { left: 277px; top: 434px; }
  .feature--dinner .feature__photo { background: linear-gradient(135deg, var(--photo-dark), var(--photo-cool)); }

  .hours {
    position: absolute; left: 0; top: 648px; width: 100%;
    color: var(--white); font-weight: 700; font-size: 13px; line-height: 15px; text-align: center;
  }

  .panel__wave { position: absolute; left: 0; top: 465px; width: 409px; height: 256px; }
  .menu-title {
    position: absolute; top: 582px; width: 100%; text-align: center;
    font-family: "Tinos", "Times New Roman", serif; font-weight: 700; font-size: 26px;
    color: var(--white); letter-spacing: 1px;
  }
</style>
</head>
<body>
  <section class="panel panel--back">
    <div class="petals" role="img" aria-label="Scattered pink cherry blossom petals"></div>
    <div class="brand">
      <span class="brand__mark"></span>
      <span class="brand__name">TSUKIHA<br>DINING</span>
    </div>
    <div class="panel__base"></div>
    <figure class="feature feature--special">
      <div class="feature__photo" role="img" aria-label="Photo of the monthly special dishes"></div>
      <div class="feature__label">Monthly Special</div>
    </figure>
    <figure class="feature feature--lunch">
      <div class="feature__photo" role="img" aria-label="Photo of the set lunch tray"></div>
      <div class="feature__label">Set Lunch</div>
    </figure>
    <figure class="feature feature--dinner">
      <div class="feature__photo" role="img" aria-label="Photo of the set dinner course"></div>
      <div class="feature__label">Set Dinner</div>
    </figure>
    <p class="hours">
      Book online or give us a call on +65 6555 0142<br>
      Lunch : 11.30am – 2.30pm (Last order: 2.15pm)<br>
      Dinner : 6.00pm – 10.30pm (Last order: 10.00pm)
    </p>
  </section>

  <section class="panel panel--front">
    <div class="petals" role="img" aria-label="Scattered pink cherry blossom petals"></div>
    <div class="brand">
      <span class="brand__mark"></span>
      <span class="brand__name">TSUKIHA<br>DINING</span>
    </div>
    <svg class="panel__wave" viewBox="0 0 409 256" preserveAspectRatio="none" aria-hidden="true">
      <path d="M0 35 Q204 -30 409 35 L409 256 L0 256 Z" fill="var(--ink)"/>
    </svg>
    <h1 class="menu-title">MENU</h1>
  </section>
</body>
</html>
```